Harbourline Electrical limited business card design

I need a business card made up it must be double sided with just my logo and some graphic one side and then on the reverse a little description of services I provide along with my email address phone number and face book and instagram handles
I already had a logo designed by pixel meadow and the social media pack so I’m thinking to use the social media design as the main image
Services I provide are: domestic commercial industrial sub contract from bathroom's and kitchen’s to outside lights and sockets no job to big or to small

Industry/Entity Type

Electrician/construction industry

Contact Information for Business Card

Email address: harbourlineelectrical@mailvane.com mobile number: 07855402917 fb: Harbourline Electrical insta: @harbourlineelectrical

Font styles to use
Sans Serif

Colors
0094D4
00A9DD
6FCCEA
C7EBF8
E9F6FB
FFF300
FFF600
FEFA6F
FFFEC7
FFFEE8

Requirements
Must have
• Double sided, fb and insta handles contact info, domestic commercial industrial sub contract
Nice to have
• From bathroom's and kitchen’s to outside outside lights and sockets no job to big or to small

```html
<!DOCTYPE html>
<html lang="en">
<head>
<meta charset="utf-8">
<title>Harbourline Electrical – Business Card</title>
<link href="https://fonts.googleapis.com/css2?family=Montserrat:wght@800&family=Lato:ital,wght@0,400;0,700;0,900;1,900&display=swap" rel="stylesheet">
<style>
  :root {
    --blue: #0094D4;
    --blue-bright: #00A9DD;
    --blue-soft: #6FCCEA;
    --gold: #E8A92C;
    --gold-light: #F6C445;
    --ink: #2b2b2b;
    --card: #ffffff;
    --backdrop: #3a3a3a;
  }
  * { box-sizing: border-box; margin: 0; padding: 0; }
  html, body { width: 1200px; height: 875px; overflow: hidden; }
  body {
    background: var(--backdrop);
    font-family: "Lato", sans-serif;
    display: flex;
    flex-direction: column;
    align-items: center;
    justify-content: center;
    gap: 56px;
  }
  .card {
    position: relative;
    width: 630px;
    height: 360px;
    background: var(--card);
    border-radius: 22px;
    overflow: hidden;
  }

  /* Front */
  .bolt-graphic {
    position: absolute;
    width: 70px;
    height: 360px;
    top: 0;
    background: linear-gradient(180deg, var(--gold-light), var(--gold));
    transform: skewX(-14deg);
  }
  .bolt-graphic--left { left: 115px; }
  .bolt-graphic--right { right: 100px; }
  .band-graphic {
    position: absolute;
    height: 34px;
    background: var(--blue);
    opacity: .85;
  }
  .band-graphic--left { left: 0; top: 210px; width: 150px; border-radius: 0 40px 40px 0; }
  .band-graphic--right { right: 0; top: 70px; width: 120px; border-radius: 40px 0 0 40px; }
  .front-mark {
    position: absolute;
    left: 50%;
    top: 50%;
    transform: translate(-50%, -50%);
    display: flex;
    flex-direction: column;
    align-items: center;
    gap: 16px;
  }
  .front-mark__circle {
    width: 96px;
    height: 96px;
    border-radius: 50%;
    border: 6px solid var(--blue);
  }
  .brand-name {
    font-family: "Montserrat", sans-serif;
    font-weight: 800;
    color: var(--blue);
    text-transform: uppercase;
    letter-spacing: .5px;
    line-height: 1;
  }
  .front-mark .brand-name { font-size: 30px; text-align: center; }

  /* Back */
  .back__info {
    position: absolute;
    left: 40px;
    top: 30px;
    width: 330px;
  }
  .back .brand-name { font-size: 25px; line-height: 1.05; }
  .person-name {
    margin-top: 14px;
    font-weight: 900;
    font-size: 24px;
    color: var(--blue);
    text-transform: uppercase;
    line-height: 1;
  }
  .person-role {
    margin-top: 3px;
    font-size: 16px;
    color: var(--gold);
  }
  .contact-list {
    list-style: none;
    margin-top: 10px;
    display: flex;
    flex-direction: column;
    gap: 3px;
  }
  .contact-list li {
    display: flex;
    align-items: center;
    gap: 9px;
    font-size: 14px;
    color: var(--ink);
  }
  .contact-list .phone-number { font-size: 17px; }
  .contact-icon { width: 14px; height: 14px; flex: none; }
  .social-dot {
    width: 12px; height: 12px; border-radius: 50%;
    background: var(--blue); flex: none; margin: 0 1px;
  }
  .back__emblem {
    position: absolute;
    right: 50px;
    top: 40px;
    width: 200px;
    height: 200px;
    border-radius: 50%;
    border: 12px solid var(--blue);
  }
  .services {
    position: absolute;
    left: 40px;
    bottom: 78px;
    font-weight: 900;
    font-size: 12px;
    letter-spacing: 1.5px;
    text-transform: uppercase;
    color: var(--gold);
  }
  .tagline {
    position: absolute;
    left: 40px;
    bottom: 34px;
    width: 470px;
    font-style: italic;
    font-weight: 900;
    font-size: 16px;
    line-height: 1.2;
    color: var(--blue);
  }
  .gold-rule {
    position: absolute;
    left: 40px;
    bottom: 18px;
    width: 420px;
    height: 7px;
    background: linear-gradient(90deg, var(--gold), var(--gold-light), var(--gold));
  }
</style>
</head>
<body>

  <section class="card front" aria-label="Card front">
    <div class="band-graphic band-graphic--left" role="img" aria-label="Blue key-pattern border graphic"></div>
    <div class="band-graphic band-graphic--right" role="img" aria-label="Blue key-pattern border graphic"></div>
    <div class="bolt-graphic bolt-graphic--left" role="img" aria-label="Gold lightning graphic"></div>
    <div class="bolt-graphic bolt-graphic--right" role="img" aria-label="Gold lightning graphic"></div>
    <div class="front-mark">
      <div class="front-mark__circle"></div>
      <p class="brand-name">Harbourline<br>Electrical</p>
    </div>
  </section>

  <section class="card back" aria-label="Card back">
    <div class="back__info">
      <p class="brand-name">Harbourline<br>Electrical</p>
      <p class="person-name">Daniel Fenwick</p>
      <p class="person-role">Founder &amp; CEO</p>
      <ul class="contact-list">
        <li class="phone-number">
          <svg class="contact-icon" viewBox="0 0 14 14" aria-hidden="true"><rect x="3" y="0.5" width="8" height="13" rx="1.5" fill="none" stroke="#0094D4" stroke-width="1.6"/><circle cx="7" cy="11" r="0.9" fill="#0094D4"/></svg>
          07855402917
        </li>
        <li>
          <svg class="contact-icon" viewBox="0 0 14 14" aria-hidden="true"><rect x="0.8" y="2.5" width="12.4" height="9" rx="1" fill="#0094D4"/><path d="M1 3 L7 8 L13 3" fill="none" stroke="#fff" stroke-width="1.2"/></svg>
          harbourlineelectrical@mailvane.com
        </li>
        <li><span class="social-dot"></span>/Harbourline Electrical</li>
        <li><span class="social-dot"></span>@harbourlineelectrical</li>
      </ul>
    </div>
    <div class="back__emblem"></div>
    <p class="services">Domestic · Commercial · Industrial · Sub Contract</p>
    <p class="tagline">From bathroom's &amp; kitchen’s to outside outside lights &amp; sockets no job to big or to small</p>
    <div class="gold-rule"></div>
  </section>

</body>
</html>
```